Wedding Thank You post card

We would like to design a thank you post card for our wedding guests.
We want it to be a classic style with our photo and a simple 'Thank you' written and then Tom and Sylvia 15.03.2014' Where the writing does not obstruct our image.
We need 140 post cards
Sorry for the delay please find some photos you can use for the design process. One or all photos can be used. Thank you
Wedding

```html
<!DOCTYPE html>
<html lang="en">
<head>
<meta charset="utf-8">
<title>Wedding Thank You Postcard – Tom &amp; Sylvia</title>
<link rel="stylesheet" href="https://fonts.googleapis.com/css2?family=Pinyon+Script&family=Cormorant+Garamond:ital,wght@1,500&display=swap">
<style>
  :root {
    --backdrop: #ece8e2;
    --card-white: #ffffff;
    --panel-charcoal: #3a3637;
    --script-green: #d6ea9c;
    --script-green-deep: #b9d37a;
    --ink-dark: #2a2627;
    --rule-taupe: #c9c2b6;
    --photo-light: #c9c6c1;
    --photo-mid: #8f8c88;
    --photo-dark: #4a4d52;
  }
  * { margin: 0; padding: 0; box-sizing: border-box; }
  html, body {
    width: 1008px; height: 1200px; overflow: hidden;
    background: var(--backdrop);
  }
  .canvas { position: relative; width: 1008px; height: 1200px; }

  .postcard {
    position: absolute; width: 614px; height: 478px;
    background: var(--card-white);
    box-shadow: 0 6px 14px rgba(0,0,0,0.18);
    overflow: hidden;
  }
  .postcard--front { left: 66px; top: 157px; }
  .postcard--back  { left: 182px; top: 652px; }

  /* Front */
  .front-photo {
    position: absolute; left: 0; top: 0; width: 382px; height: 100%;
    background: linear-gradient(160deg, var(--photo-light) 0%, var(--photo-mid) 45%, var(--photo-dark) 100%);
  }
  .front-panel {
    position: absolute; left: 382px; top: 0; width: 232px; height: 100%;
    background: var(--panel-charcoal);
    color: var(--script-green);
  }
  .front-title {
    position: absolute; font-family: "Pinyon Script", cursive;
    font-size: 78px; line-height: 1; font-weight: 400;
  }
  .front-title--thank { left: 6px; top: 24px; }
  .front-title--you { left: 86px; top: 138px; }
  .front-message {
    position: absolute; left: 0; top: 318px; width: 100%;
    text-align: center; font-family: "Cormorant Garamond", serif;
    font-style: italic; font-weight: 500; font-size: 15px; line-height: 20px;
  }
  .front-names {
    position: absolute; left: 0; top: 372px; width: 100%; text-align: center;
    font-family: "Pinyon Script", cursive; font-size: 30px;
  }
  .front-names .amp { font-size: 20px; margin: 0 4px; }
  .front-date {
    position: absolute; left: 0; top: 426px; width: 100%; text-align: center;
    font-family: "Cormorant Garamond", serif; font-style: italic; font-weight: 500; font-size: 16px;
  }

  /* Back */
  .back-title {
    position: absolute; left: 30px; top: 40px;
    font-family: "Pinyon Script", cursive; font-size: 52px; line-height: 1;
    color: var(--script-green-deep);
    text-shadow: 2px 2px 0 rgba(60,60,40,0.35);
  }
  .back-rule {
    position: absolute; left: 32px; top: 137px; width: 250px; height: 1px;
    background: var(--rule-taupe);
  }
  .back-names {
    position: absolute; font-family: "Pinyon Script", cursive; color: var(--ink-dark);
    line-height: 1;
  }
  .back-names--first { left: 60px; top: 168px; font-size: 44px; }
  .back-names--amp { left: 140px; top: 220px; font-size: 20px; }
  .back-names--second { left: 92px; top: 242px; font-size: 44px; }
  .back-divider {
    position: absolute; left: 305px; top: 42px; width: 1px; height: 392px;
    background: var(--rule-taupe);
  }
  .stamp-box {
    position: absolute; left: 510px; top: 29px; width: 76px; height: 90px;
    border: 1.5px solid var(--rule-taupe);
  }
  .address-line {
    position: absolute; left: 333px; width: 252px; height: 1.5px;
    background: var(--rule-taupe);
  }
</style>
</head>
<body>
<main class="canvas">
  <section class="postcard postcard--front">
    <div class="front-photo" role="img" aria-label="Wedding photo of the bride and groom embracing outside a stone building"></div>
    <div class="front-panel">
      <h1 class="front-title front-title--thank">Thank</h1>
      <span class="front-title front-title--you">You</span>
      <p class="front-message">For Sharing In Our Joy<br>On Our Special Day</p>
      <p class="front-names">Tom <span class="amp">&amp;</span>Sylvia</p>
      <p class="front-date">15.03.2014</p>
    </div>
  </section>

  <section class="postcard postcard--back">
    <h2 class="back-title">Thank You</h2>
    <div class="back-rule"></div>
    <p class="back-names back-names--first">Tom</p>
    <p class="back-names back-names--amp">&amp;</p>
    <p class="back-names back-names--second">Sylvia</p>
    <div class="back-divider"></div>
    <div class="stamp-box"></div>
    <div class="address-line" style="top:186px"></div>
    <div class="address-line" style="top:238px"></div>
    <div class="address-line" style="top:290px"></div>
    <div class="address-line" style="top:342px"></div>
  </section>
</main>
</body>
</html>
```